Taking action and overcoming fear with changes in your life. Encouraging people to make a change ...

I need a logo and basic website done in wordpress for my website brightstepforward.example. I would like an image or images showing action and overcoming fear. This is an encouragement site to motivate and inspire. Images showing challenges and overcoming challenges. Bright and exciting. Please use your own creativity.

Font styles to use
Sans Serif

Colors

Designer to choose colors to be used in the design.

```html
<!DOCTYPE html>
<html lang="en">
<head>
<meta charset="utf-8">
<title>Bright Step Forward</title>
<link href="https://fonts.googleapis.com/css2?family=Barlow:ital,wght@0,400;0,500;0,600;0,700;1,400&display=swap" rel="stylesheet">
<style>
:root{
  --accent:#e0481a;
  --orange-1:#e8892b;
  --orange-2:#fb7311;
  --orange-3:#e9643a;
  --orange-4:#e04515;
  --ink:#2a2a2a;
  --body:#555;
  --light-bg:#f1f1f1;
  --footer:#1b1b1b;
  --white:#fff;
}
*{margin:0;padding:0;box-sizing:border-box}
html,body{width:1200px;height:3582px;overflow:hidden}
body{font-family:'Barlow',sans-serif;color:var(--ink);position:relative;background:var(--white)}
.abs{position:absolute}
.btn{position:absolute;background:var(--accent);color:var(--white);font-weight:700;font-size:14px;display:flex;align-items:center;justify-content:center;letter-spacing:.2px}

/* hero */
.hero{left:0;top:0;width:1200px;height:606px;background:linear-gradient(180deg,#6d4c3c 0%,#c98353 35%,#a15a3a 60%,#3b2a24 85%,#2a2220 100%)}
.brand{left:172px;top:25px;font-size:25px;line-height:30px;font-weight:700;color:var(--white);white-space:nowrap}
.nav{left:495px;top:31px;display:flex;gap:27px;font-size:14px;color:var(--white);font-weight:500;white-space:nowrap}
.login{left:943px;top:26px;width:85px;height:27px;border:2px solid var(--white);border-radius:14px;color:var(--white);font-size:13px;font-weight:700;display:flex;align-items:center;justify-content:center;gap:4px}
.hero-title{left:172px;top:222px;font-size:46px;line-height:49px;font-weight:700;color:var(--white);letter-spacing:.5px}
.hero-arrow{top:264px;width:34px;height:34px;border:1.5px solid var(--white);border-radius:50%}

/* features */
.feature{top:606px;width:300px;height:300px;color:var(--white)}
.feature svg.icon{position:absolute;left:34px;top:40px}
.feature h3{position:absolute;left:34px;top:128px;font-size:18px;line-height:23px;font-weight:700;width:250px}
.feature p{position:absolute;left:34px;top:186px;font-size:11px;line-height:20px;width:212px}
.feature .arrow{position:absolute;left:36px;top:258px}

/* about */
.about{left:0;top:906px;width:1200px;height:643px;background:var(--light-bg)}
.section-title{font-size:39px;font-weight:700;color:var(--ink)}
.text{font-size:12.5px;line-height:22.4px;color:var(--body)}

/* what we do */
.card-img{top:1757px;width:260px;height:206px}
.card h3{position:absolute;top:1980px;font-size:18px;font-weight:700}
.card .rule{position:absolute;top:2017px;width:64px;height:2px;background:var(--accent)}
.card p{position:absolute;top:2030px;width:260px}

/* testimonial */
.testimonial{left:0;top:2310px;width:1200px;height:435px;background:linear-gradient(180deg,#e1ab8c 0%,#c59a88 35%,#7f7e7f 65%,#3f4a52 100%)}
.quote{left:391px;top:2462px;width:520px;font-size:17.5px;line-height:25.5px;font-style:italic;color:#f3efee}
.author{left:391px;top:2628px;font-size:18px;font-weight:700;color:var(--white)}

/* footer */
.footer{left:0;top:3285px;width:1200px;height:297px;background:var(--footer)}
.footer-nav{left:0;top:3492px;width:1200px;display:flex;justify-content:center;gap:27px;font-size:13px;color:#ddd}
.copy{left:0;top:3530px;width:1200px;text-align:center;font-size:12.5px;color:#ddd}
</style>
</head>
<body>

<!-- hero -->
<div class="abs hero" role="img" aria-label="Silhouettes of two climbers, one helping the other up a rocky ridge at sunset"></div>
<div class="abs brand">BRIGHT STEP FORWARD</div>
<div class="abs nav"><span>HOME</span><span>ABOUT</span><span>WHAT WE DO</span><span>WHY CHOOSE US?</span><span>CONTACT</span></div>
<div class="abs login">
  <svg width="10" height="11" viewBox="0 0 10 11"><circle cx="5" cy="3" r="2.6" fill="#fff"/><path d="M0 11 C0 6.5 10 6.5 10 11Z" fill="#fff"/></svg>LOGIN
</div>
<h1 class="abs hero-title">ENCOURAGING<br>PEOPLE TO MAKE<br>A CHANGE</h1>
<div class="abs hero-arrow" style="left:25px"><svg width="31" height="31" viewBox="0 0 31 31"><path d="M18 10 L13 15.5 L18 21" stroke="#fff" stroke-width="1.5" fill="none"/></svg></div>
<div class="abs hero-arrow" style="left:1148px"><svg width="31" height="31" viewBox="0 0 31 31"><path d="M13 10 L18 15.5 L13 21" stroke="#fff" stroke-width="1.5" fill="none"/></svg></div>

<!-- features -->
<div class="abs feature" style="left:0;background:var(--orange-1)">
  <svg class="icon" width="50" height="64" viewBox="0 0 50 64" fill="none" stroke="#fff" stroke-width="3"><path d="M3 62 L24 24 L46 62 Z"/><path d="M24 24 V3 H42 L38 9 L42 15 H24"/><path d="M13 44 L20 50 L25 42 L31 50 L36 44"/></svg>
  <h3>Lorem ipsum dolor sam consectetur adipis</h3>
  <p>At vero eos et accusamus et iusto oiss imos olores et quas molestias excepoc aecati cupiditate similique.</p>
  <svg class="arrow" width="22" height="10" viewBox="0 0 22 10"><path d="M0 5 H20 M15 1 L20 5 L15 9" stroke="#fff" stroke-width="1.6" fill="none"/></svg>
</div>
<div class="abs feature" style="left:300px;background:var(--orange-2)">
  <svg class="icon" width="56" height="64" viewBox="0 0 56 64" fill="none" stroke="#fff" stroke-width="2.6"><path d="M14 62 V48 C4 42 2 30 6 20 C12 4 38 0 48 16 C52 22 50 28 54 34 L48 36 V44 C48 48 44 50 38 48 V62"/><circle cx="22" cy="20" r="4"/><circle cx="34" cy="18" r="4"/><circle cx="28" cy="30" r="4"/><circle cx="16" cy="32" r="3"/><circle cx="40" cy="30" r="3"/></svg>
  <h3>Lorem ipsum dolor sam consectetur adipis</h3>
  <p>At vero eos et accusamus et iusto oiss imos olores et quas molestias excepoc aecati cupiditate similique.</p>
  <svg class="arrow" width="22" height="10" viewBox="0 0 22 10"><path d="M0 5 H20 M15 1 L20 5 L15 9" stroke="#fff" stroke-width="1.6" fill="none"/></svg>
</div>
<div class="abs feature" style="left:600px;background:var(--orange-3)">
  <svg class="icon" width="66" height="64" viewBox="0 0 66 64" fill="none" stroke="#fff" stroke-width="3"><circle cx="30" cy="34" r="27"/><circle cx="30" cy="34" r="18"/><circle cx="30" cy="34" r="9"/><path d="M30 34 L58 6 M52 4 L58 6 L60 12"/></svg>
  <h3>Lorem ipsum dolor sam consectetur adipis</h3>
  <p>At vero eos et accusamus et iusto oiss imos olores et quas molestias excepoc aecati cupiditate similique.</p>
  <svg class="arrow" width="22" height="10" viewBox="0 0 22 10"><path d="M0 5 H20 M15 1 L20 5 L15 9" stroke="#fff" stroke-width="1.6" fill="none"/></svg>
</div>
<div class="abs feature" style="left:900px;background:var(--orange-4)">
  <svg class="icon" width="66" height="64" viewBox="0 0 66 64" fill="none" stroke="#fff" stroke-width="2.6"><circle cx="34" cy="8" r="5"/><path d="M32 14 L24 30 L34 36 L28 52 M24 30 L12 34 L6 46 M30 20 L42 24 L50 18"/><path d="M4 60 L22 42 L34 50 L60 22 M52 22 H60 V30"/></svg>
  <h3>Lorem ipsum dolor sam consectetur adipis</h3>
  <p>At vero eos et accusamus et iusto oiss imos olores et quas molestias excepoc aecati cupiditate similique.</p>
  <svg class="arrow" width="22" height="10" viewBox="0 0 22 10"><path d="M0 5 H20 M15 1 L20 5 L15 9" stroke="#fff" stroke-width="1.6" fill="none"/></svg>
</div>

<!-- about -->
<div class="abs about"></div>
<div class="abs" style="left:160px;top:990px;width:414px;height:474px;background:#d6d6d6"></div>
<div class="abs" style="left:172px;top:973px;width:422px;height:481px;background:linear-gradient(180deg,#7d8086 0%,#9a9ca0 40%,#8a7f74 70%,#6a6258 100%)" role="img" aria-label="Businessman standing on the top of a tall rock against a cloudy sky"></div>
<h2 class="abs section-title" style="left:649px;top:1010px">About Us</h2>
<p class="abs text" style="left:648px;top:1080px;width:370px">Sed ut perspiciatis unde omnis iste natus error sit voluptatem accusantium doloremque laudantium, totam rem aperiam, eaque ipsa quae ab illo inventore veritatis et quasi architecto beatae vit ae dicta sunt explicabo. Nemo enim ipsam voluptatem quia volupt as sit aspernatur aut odit aut fugit, sed quia consequuntur magni dolores eos qui ratione voluptatem sequi nesciunt. Neque porro quisquam est, qui dolorem ipsum quia dolor sit amet, consectetur , adipisci velit, sed quia non numquam eius modi tempora incidunt labore et dolore magnam aliquam quaerat voluptatem enim ad mi nima veniam, quis nostrum exercitationem ullam corporis suscipit laboriosam, nisi ut aliquid ex ea commodi consequatuuis autemel eum iure reprehenderit qui in ea voluptate velit</p>
<div class="btn" style="left:648px;top:1376px;width:108px;height:39px">READ MORE</div>

<!-- what we do -->
<h2 class="abs section-title" style="left:0;width:1200px;text-align:center;top:1624px">What We Do</h2>
<p class="abs text" style="left:0;width:1200px;text-align:center;top:1690px">Sed ut perspiciatis unde omnis iste natus error sit voluptatem accusantium dolorlaudantium<br>totam rem aperiam, eaque ipsa quae ab illo inventore veritatis et quasi architect.</p>

<div class="card">
  <div class="abs card-img" style="left:172px;background:linear-gradient(180deg,#c5714a 0%,#e59a55 55%,#f6a531 75%,#2b1a12 100%)" role="img" aria-label="Silhouette of a person leaping across a gap between two cliffs at sunset"></div>
  <h3 style="left:172px">Suptatem accusantium</h3>
  <div class="rule" style="left:172px"></div>
  <p class="text" style="left:172px">Sed ut perspiciatis unde omnis iste natu serror sit voluptatem accusantium dolorlau dantiumtotam rem aperiam, eaque ipsa quae ab illo inventore veritatis et quastam rem aperiam, eaque ipsa quae.</p>
  <div class="btn" style="left:172px;top:2155px;width:109px;height:38px">READ MORE</div>
</div>
<div class="card">
  <div class="abs card-img" style="left:467px;background:linear-gradient(180deg,#1d5fa8 0%,#4d8ac6 40%,#c9c4be 70%,#e6e2dc 100%)" role="img" aria-label="Hiker in a red jacket raising both arms on a snowy mountain peak"></div>
  <h3 style="left:467px">Suptatem accusantium</h3>
  <div class="rule" style="left:467px"></div>
  <p class="text" style="left:467px">Sed ut perspiciatis unde omnis iste natu serror sit voluptatem accusantium dolorlau dantiumtotam rem aperiam, eaque ipsa quae ab illo inventore veritatis et quastam rem aperiam, eaque ipsa quae.</p>
  <div class="btn" style="left:467px;top:2155px;width:109px;height:38px">READ MORE</div>
</div>
<div class="card">
  <div class="abs card-img" style="left:763px;background:linear-gradient(135deg,#2b2f33 0%,#45494d 50%,#2c2f32 100%)" role="img" aria-label="Businessman at a chalkboard covered with a target and strategy sketches"></div>
  <h3 style="left:763px">Suptatem accusantium</h3>
  <div class="rule" style="left:763px"></div>
  <p class="text" style="left:763px">Sed ut perspiciatis unde omnis iste natu serror sit voluptatem accusantium dolorlau dantiumtotam rem aperiam, eaque ipsa quae ab illo inventore veritatis et quastam rem aperiam, eaque ipsa quae.</p>
  <div class="btn" style="left:763px;top:2155px;width:109px;height:38px">READ MORE</div>
</div>

<!-- testimonial -->
<div class="abs testimonial" role="img" aria-label="Man standing on a rock overlooking misty mountains at dawn"></div>
<svg class="abs" style="left:281px;top:2453px" width="78" height="50" viewBox="0 0 78 50"><g fill="#fff"><circle cx="16" cy="34" r="15"/><path d="M2 34 C2 14 12 4 28 0 L30 5 C20 9 14 17 16 34Z"/><circle cx="58" cy="34" r="15"/><path d="M44 34 C44 14 54 4 70 0 L72 5 C62 9 56 17 58 34Z"/></g></svg>
<p class="abs quote">Sed ut perspiciatis unde omnis iste natus error sit voluptatem accusantium doloremque laudantium, totam rem aperiam, eaque ipsa quae ab illo inventore veritatis et quasi architecto beatae vit ae dicta sunt explicabo. Nemo enim ipsam voluptatem quia volupt as sit aspernatur aut odit aut fugit, sed quia consequuntur eos ratione voluptatem sequi nesciunt.</p>
<div class="abs author">– Dana Rivers City Name</div>
<svg class="abs" style="left:986px;top:2686px" width="42" height="30" viewBox="0 0 42 30"><path d="M12 2 L2 15 L12 28 M30 2 L40 15 L30 28" stroke="#fff" stroke-width="1.5" fill="none"/></svg>

<!-- why choose us -->
<h2 class="abs section-title" style="left:172px;top:2842px">Why Choose Us?</h2>
<p class="abs text" style="left:172px;top:2901px;width:340px">Sed ut perspiciatis unde omnis iste natus error sit voluptat em accusantium doloremque laudantium, totam rem aperia ae dicta sunt explicabo. Nemo enim ipsam voluptatem quia oluptas sit aspernatur aut odit aut fugit, sed quia consequun tur magni dolores eos qui ratione voluptatem sequi nesciunt Neque porro quisquam est, qui dolorem ipsum quia dolor s it amet, consectetur, adipisci velitptas sit aspernatur aut o dit aut fugit, sed quia consequuntur magni dolores eos qui ratione voluptatem sequi nesciuntue porro quisquam est, qui dolorem ipsum qet, consectetu.</p>
<div class="btn" style="left:171px;top:3141px;width:108px;height:38px">READ MORE</div>
<div class="abs" style="left:607px;top:2871px;width:427px;height:325px;background:#d6d6d6"></div>
<div class="abs" style="left:546px;top:2859px;width:481px;height:327px;background:linear-gradient(180deg,#6f9fd0 0%,#9cc0e2 55%,#b7c6cf 80%,#8c9aa2 100%)" role="img" aria-label="Smiling rock climber with gear standing beside a cliff under a blue sky"></div>
<svg class="abs" style="left:746px;top:2981px" width="82" height="82" viewBox="0 0 82 82"><circle cx="41" cy="41" r="38" fill="rgba(0,0,0,.25)" stroke="#fff" stroke-width="4"/><path d="M32 24 L58 41 L32 58Z" fill="none" stroke="#fff" stroke-width="4"/></svg>

<!-- footer -->
<div class="abs footer"></div>
<h2 class="abs" style="left:0;width:1200px;text-align:center;top:3308px;font-size:39px;font-weight:700;color:#fff">Subscribe Newsletter</h2>
<div class="abs" style="left:360px;top:3378px;width:356px;height:39px;background:#fff;font-size:11px;color:#555;padding:12px 10px">Email:</div>
<div class="btn" style="left:724px;top:3378px;width:116px;height:39px">SIGN UP</div>
<svg class="abs" style="left:553px;top:3444px" width="96" height="32" viewBox="0 0 96 32" role="img" aria-label="Social media links"><g fill="none" stroke="#fff" stroke-width="1.5"><circle cx="16" cy="16" r="14"/><circle cx="47" cy="16" r="14"/><circle cx="78" cy="16" r="14"/></g></svg>
<div class="abs footer-nav"><span>HOME</span><span>ABOUT</span><span>WHAT WE DO</span><span>WHY CHOOSE US?</span><span>CONTACT</span></div>
<div class="abs copy">© 2019 All Rights are Reserved. Privacy Policy | Terms of Use | Site map</div>

</body>
</html>
```